Zoom Background

Short project summary

Quilvane (public-safety / law-enforcement SaaS) needs clean, camera-friendly, on-brand virtual backgrounds and a print-ready backdrop design our sales team will use during demos, client meetings, and trade events. The look should reinforce trust, tech professionalism, and be optimized so the presenter’s face stays the focal point.

Deliverables (required)

Primary Zoom background (16:9) — static
1920×1080 PNG (RGB) and 3840×2160 PNG (4K).
Two alternative concepts (total 3 concepts delivered as above).
Lower-third overlay (transparent PNG) or layered PSD/AI template for name/title.
Source files: layered AI or PSD for every concept.

One-page usage notes: recommended camera framing, safe area diagrams, and Zoom export settings.

File / technical specs

Aspect ratio: 16:9 for digital backgrounds.
Static files: PNG (transparent elements permitted where useful). Keep static PNGs ideally <5 MB.
Print files: PDF (CMYK), 300 DPI, include crop marks and 0.125" bleed. Fonts outlined or embedded.

Safe area guidance: keep critical text/logos inside central ~60% width × 50% height; avoid placing important elements behind where a presenter’s head will appear.

Provide HEX color codes and font names used (Pantone advisable if available).

Brand / tone / constraints
Tone: confident, professional, trustworthy, modern — designed for law-enforcement and public-safety buyers.
Use Quilvane brand assets (logo, color palette, type) — we will supply high-res logos, colors, and fonts.

Do not include any sensitive or personally identifiable data (no case numbers, police records, photos of people without release).

Submission requirements

Upload final PNG(s) and AI/PSD source files.
Include a short note (1–2 sentences) describing how each concept works on camera.
Provide one screenshot mock showing a presenter over the background (head & shoulders) — or a photo mockup.

Thank you to everyone who has submitted so far. I appreciate the time and creativity that’s gone into your designs, but I’d like to provide clearer direction on what I’m looking for so we can get closer to Quilvane’s brand vision.

Most of the current submissions don’t yet capture the technological, professional, and futuristic tone we need. Quilvane is a public-safety / law-enforcement SaaS company - our look should feel advanced, trustworthy, and tech-driven, not cartoonish or generic.

What I’m Looking For
A clean, modern, and futuristic design that conveys innovation and authority.
Think “next-gen law enforcement intelligence platform” rather than a traditional or corporate background.
I’d love to see more use of light effects, gradients, depth, and subtle motion-inspired elements—something that feels like it could exist in a holographic interface or augmented-reality environment.
A concept where “Quilvane” appears to subtly emerge or project from the background, almost like a holographic or glowing element, would be ideal.

Please Avoid
Cartoonish or clip-art styles
Plain or overly flat designs with little visual interest
Ignoring the provided Quilvane brand assets (logo, colors, typography)

Still Required
As a reminder, final submissions should include:
3 concepts (1920×1080 and 3840×2160 PNGs)
Lower-third overlay (transparent PNG or layered PSD/AI)
Layered source files (AI or PSD)
One-page usage notes (camera framing, safe area, etc.)

Inspiration Keywords
Clean • Futuristic • Secure • Holographic • Connected • Precision • Law-enforcement tech • Data-driven

```html
<!DOCTYPE html>
<html lang="en">
<head>
<meta charset="utf-8">
<title>Quilvane Virtual Background</title>
<link rel="stylesheet" href="https://fonts.googleapis.com/css2?family=Exo+2:wght@500&display=swap">
<style>
  :root {
    --void: #070d14;
    --wall-deep: #0a1826;
    --wall-mid: #0f2236;
    --teal-dark: #123a40;
    --teal: #2a7a84;
    --teal-light: #3a8f99;
    --frame: #020406;
    --glow: #6fd8f2;
    --glow-soft: #4fc3e0;
    --panel-deep: #06262a;
    --panel-mid: #0c4a48;
  }
  html, body {
    margin: 0;
    padding: 0;
    width: 1200px;
    height: 675px;
    overflow: hidden;
    background: var(--void);
  }
  .room {
    position: relative;
    width: 1200px;
    height: 675px;
  }
  .room svg { display: block; }
  .brand-name {
    font-family: "Exo 2", sans-serif;
    font-weight: 500;
    font-size: 46px;
    letter-spacing: 4px;
    fill: var(--glow);
  }
</style>
</head>
<body>
<div class="room">
  <svg width="1200" height="675" viewBox="0 0 1200 675" xmlns="http://www.w3.org/2000/svg">
    <defs>
      <linearGradient id="ceiling-sheen" x1="0" y1="0" x2="1" y2="0">
        <stop offset="0" stop-color="var(--teal-dark)"/>
        <stop offset="0.3" stop-color="var(--teal)"/>
        <stop offset="0.55" stop-color="#10282c"/>
        <stop offset="0.8" stop-color="var(--teal-light)"/>
        <stop offset="1" stop-color="var(--teal)"/>
      </linearGradient>
      <linearGradient id="floor-sheen" x1="0" y1="0" x2="1" y2="0">
        <stop offset="0" stop-color="var(--teal)"/>
        <stop offset="0.35" stop-color="var(--teal-light)"/>
        <stop offset="0.6" stop-color="#174a50"/>
        <stop offset="1" stop-color="var(--teal-light)"/>
      </linearGradient>
      <linearGradient id="back-wall" x1="0" y1="0" x2="1" y2="1">
        <stop offset="0" stop-color="var(--wall-deep)"/>
        <stop offset="0.5" stop-color="var(--wall-mid)"/>
        <stop offset="1" stop-color="#08121c"/>
      </linearGradient>
      <linearGradient id="side-glass" x1="0" y1="0" x2="0" y2="1">
        <stop offset="0" stop-color="#16384a"/>
        <stop offset="0.5" stop-color="#0f2c3c"/>
        <stop offset="1" stop-color="#1a4656"/>
      </linearGradient>
      <linearGradient id="panel-fill" x1="0" y1="0" x2="1" y2="1">
        <stop offset="0" stop-color="var(--panel-mid)"/>
        <stop offset="0.5" stop-color="var(--panel-deep)"/>
        <stop offset="1" stop-color="#0e5652"/>
      </linearGradient>
      <filter id="glow" x="-20%" y="-20%" width="140%" height="140%">
        <feGaussianBlur stdDeviation="4" result="b"/>
        <feMerge><feMergeNode in="b"/><feMergeNode in="SourceGraphic"/></feMerge>
      </filter>
      <filter id="soft" x="-50%" y="-50%" width="200%" height="200%">
        <feGaussianBlur stdDeviation="2.5"/>
      </filter>
    </defs>

    <!-- ceiling -->
    <polygon class="ceiling" points="0,0 1200,0 1200,28 1045,115 156,115 0,28" fill="url(#ceiling-sheen)"/>
    <g class="ceiling-streaks" stroke="var(--glow-soft)" stroke-width="3" stroke-linecap="round" opacity="0.55" filter="url(#soft)">
      <line x1="225" y1="2" x2="237" y2="42"/>
      <line x1="323" y1="8" x2="340" y2="60"/>
      <line x1="670" y1="2" x2="668" y2="42"/>
      <line x1="890" y1="2" x2="876" y2="45"/>
    </g>

    <!-- floor -->
    <polygon class="floor" points="156,552 1045,552 1200,640 1200,675 0,675 0,640" fill="url(#floor-sheen)"/>
    <g class="floor-streaks" stroke="var(--glow-soft)" stroke-width="3" stroke-linecap="round" opacity="0.45" filter="url(#soft)">
      <line x1="278" y1="615" x2="270" y2="665"/>
      <line x1="380" y1="625" x2="374" y2="670"/>
    </g>

    <!-- left wall -->
    <polygon class="wall-left" points="0,28 156,115 156,552 0,640" fill="var(--frame)"/>
    <polygon class="wall-left-glass" points="0,68 144,148 144,540 0,585" fill="url(#side-glass)" stroke="var(--glow-soft)" stroke-opacity="0.5" stroke-width="2"/>

    <!-- right wall -->
    <polygon class="wall-right" points="1200,28 1045,115 1045,552 1200,640" fill="var(--frame)"/>
    <polygon class="wall-right-glass" points="1200,72 1056,148 1056,545 1200,590" fill="url(#side-glass)" stroke="var(--glow-soft)" stroke-opacity="0.5" stroke-width="2"/>

    <!-- back wall frame and surface -->
    <rect class="back-wall-frame" x="150" y="112" width="901" height="448" fill="var(--frame)"/>
    <rect class="back-wall" x="158" y="136" width="887" height="414" fill="url(#back-wall)" role="img" aria-label="Dark navy low-poly faceted wall texture"/>

    <!-- light streaks -->
    <g class="light-streaks" stroke="var(--glow)" stroke-width="2.5" stroke-linecap="round" filter="url(#glow)">
      <line x1="327" y1="213" x2="327" y2="287"/>
      <line x1="235" y1="295" x2="235" y2="368"/>
      <line x1="277" y1="432" x2="277" y2="505"/>
      <line x1="532" y1="216" x2="532" y2="231"/>
      <line x1="856" y1="193" x2="856" y2="265"/>
      <line x1="953" y1="216" x2="953" y2="289"/>
      <line x1="381" y1="480" x2="381" y2="492"/>
    </g>

    <!-- hologram panel -->
    <g class="holo-panel">
      <rect x="354" y="228" width="493" height="256" rx="4" fill="none" stroke="var(--glow-soft)" stroke-width="6" opacity="0.6" filter="url(#soft)"/>
      <rect x="356" y="230" width="489" height="252" rx="3" fill="url(#panel-fill)" role="img" aria-label="Teal low-poly faceted hologram backdrop"/>
      <rect x="356" y="230" width="489" height="252" rx="3" fill="none" stroke="var(--glow)" stroke-width="2"/>
      <text class="brand-name" x="600" y="372" text-anchor="middle">Quilvane</text>
    </g>
  </svg>
</div>
</body>
</html>
```